Brightmark Electrical Flyer

An eye catching flyer design which showcases the type of work we do in the electrical industry in Vancouver,BC. The final design should be simple and incorporate our logo. And present a high end company.

Industry/Entity Type

Electrical

```html
<!DOCTYPE html>
<html lang="en">
<head>
<meta charset="utf-8">
<title>Brightmark Electrical Flyer</title>
<link href="https://fonts.googleapis.com/css2?family=Arvo:wght@700&family=Open+Sans:ital,wght@0,400;0,600;0,700;1,600&display=swap" rel="stylesheet">
<style>
  :root {
    --yellow: #f7d117;
    --charcoal: #262626;
    --black: #111111;
    --white: #ffffff;
    --stage: #e9e7e3;
    --photo-top: #d9dde2;
    --photo-bottom: #9aa3ad;
    --crew-top: #c9a46a;
    --crew-bottom: #3d4f7a;
  }
  * { margin: 0; padding: 0; box-sizing: border-box; }
  html, body { width: 907px; height: 1200px; overflow: hidden; }
  body { background: var(--stage); font-family: "Open Sans", Arial, sans-serif; position: relative; }

  .flyer { position: absolute; left: 44px; top: 72px; width: 817px; height: 1058px; background: var(--charcoal); overflow: hidden; }

  .hero-photo { position: absolute; left: 0; top: 0; width: 817px; height: 368px;
    background: linear-gradient(160deg, var(--photo-top) 0%, #eef0f2 45%, var(--photo-bottom) 100%); }
  .hero-edge { position: absolute; left: 0; top: 325px; width: 817px; height: 50px; }

  .brand-top { position: absolute; right: 32px; top: 52px; text-align: right; color: var(--charcoal); }
  .brand-name { font-family: "Open Sans", Arial, sans-serif; font-weight: 700; font-size: 26px; line-height: 1; display: flex; align-items: center; gap: 8px; justify-content: flex-end; }
  .brand-mark { width: 14px; height: 14px; background: var(--yellow); border-radius: 50%; display: inline-block; }
  .brand-url { font-weight: 700; font-size: 15px; margin-top: 6px; }

  .tab { position: absolute; left: 0; width: 234px; height: 37px; background: var(--yellow);
    clip-path: polygon(0 0, 212px 0, 234px 100%, 0 100%);
    font-family: "Arvo", Georgia, serif; font-weight: 700; font-size: 20px; color: var(--black);
    padding-left: 28px; line-height: 37px; letter-spacing: 0.3px; }
  .tab-what { top: 385px; }
  .tab-who { top: 591px; }

  .services { position: absolute; left: 36px; top: 430px; list-style: none; }
  .services li { color: var(--white); font-size: 14px; height: 24px; line-height: 24px; display: flex; align-items: center; gap: 9px; }
  .services svg { width: 11px; height: 11px; flex: none; }

  .divider { position: absolute; left: 441px; top: 438px; width: 2px; height: 131px; background: var(--yellow); }

  .headline { position: absolute; right: 21px; top: 387px; text-align: right; font-family: "Arvo", Georgia, serif; font-weight: 700; }
  .headline-main { color: var(--yellow); font-size: 34px; line-height: 43px; letter-spacing: 1px; }
  .headline-place { color: var(--white); font-size: 26px; line-height: 40px; }
  .headline-tag { font-family: "Open Sans", Arial, sans-serif; font-style: italic; font-weight: 600; color: var(--white); font-size: 44px; line-height: 60px; margin-top: 22px; }

  .about { position: absolute; left: 35px; top: 642px; width: 432px; color: var(--white); font-size: 12.9px; line-height: 18px; }

  .white-zone { position: absolute; left: 0; top: 755px; width: 817px; height: 165px; background: var(--white); }
  .yellow-strip { position: absolute; left: 0; top: 743px; width: 462px; height: 18px; background: var(--yellow);
    clip-path: polygon(0 0, 100% 0, 448px 100%, 0 100%); }

  .brand-bottom { position: absolute; left: 72px; top: 806px; color: var(--charcoal); }
  .brand-bottom .brand-name { justify-content: flex-start; font-size: 24px; }
  .brand-bottom .brand-url { font-size: 14.5px; }

  .crew-photo { position: absolute; left: 470px; top: 596px; width: 347px; height: 324px;
    background: linear-gradient(180deg, var(--crew-top) 0%, #6f7fa6 55%, var(--crew-bottom) 100%); }

  .footer { position: absolute; left: 0; top: 920px; width: 817px; height: 138px; background: var(--black); }
  .name-bar { position: absolute; left: 0; top: 0; width: 434px; height: 58px; background: var(--yellow);
    clip-path: polygon(0 0, 412px 0, 434px 100%, 0 100%); }
  .contact-name { position: absolute; left: 20px; top: 2px; font-weight: 700; font-size: 45px; line-height: 56px; color: var(--black); }
  .call { position: absolute; left: 20px; top: 74px; font-weight: 600; font-size: 32px; color: var(--white); }
  .contact-list { position: absolute; left: 467px; top: 30px; list-style: none; }
  .contact-list li { display: flex; align-items: center; gap: 8px; color: var(--white); font-size: 22px; line-height: 32px; }
  .contact-list svg { width: 19px; height: 19px; flex: none; }
</style>
</head>
<body>
  <main class="flyer">
    <div class="hero-photo" role="img" aria-label="Close-up photo of a row of circuit breakers with blue, red and black wires"></div>
    <svg class="hero-edge" viewBox="0 0 817 50" preserveAspectRatio="none" aria-hidden="true">
      <polygon points="0,28 340,28 405,4 470,28 817,28 817,50 0,50" fill="var(--charcoal)"/>
      <polygon points="0,28 340,28 405,4 470,28 817,28 817,43 470,43 405,22 340,43 0,43" fill="var(--yellow)"/>
    </svg>

    <div class="brand-top">
      <div class="brand-name"><span class="brand-mark"></span>Brightmark Electrical</div>
      <div class="brand-url">www.brightmarkelectrical.ca</div>
    </div>

    <h2 class="tab tab-what">WHAT WE DO</h2>
    <ul class="services">
      <li><svg viewBox="0 0 10 10"><polygon points="0,0 10,5 0,10 3,5" fill="var(--yellow)"/></svg>Lorem Ipsum is simply dummy text of the printing</li>
      <li><svg viewBox="0 0 10 10"><polygon points="0,0 10,5 0,10 3,5" fill="var(--yellow)"/></svg>Lorem Ipsum is simply dummy text of the printing</li>
      <li><svg viewBox="0 0 10 10"><polygon points="0,0 10,5 0,10 3,5" fill="var(--yellow)"/></svg>Lorem Ipsum is simply dummy text of the printing</li>
      <li><svg viewBox="0 0 10 10"><polygon points="0,0 10,5 0,10 3,5" fill="var(--yellow)"/></svg>Lorem Ipsum is simply dummy text of the printing</li>
      <li><svg viewBox="0 0 10 10"><polygon points="0,0 10,5 0,10 3,5" fill="var(--yellow)"/></svg>Lorem Ipsum is simply dummy text of the printing</li>
      <li><svg viewBox="0 0 10 10"><polygon points="0,0 10,5 0,10 3,5" fill="var(--yellow)"/></svg>Lorem Ipsum is simply dummy text of the printing</li>
    </ul>
    <div class="divider"></div>

    <div class="headline">
      <div class="headline-main">ELECTRICAL<br>INDUSTRY</div>
      <div class="headline-place">in Vancouver,BC</div>
      <div class="headline-tag">Lorem Ipsum</div>
    </div>

    <h2 class="tab tab-who">WHO WE ARE</h2>
    <p class="about">Lorem Ipsum is simply dummy text of the printing and typesetting industry. Lorem Ipsum has been the industry's standard dummy text ever since the 1500s, when an unknown printer took a galley of type and scrambled it to make a type specimen book</p>

    <div class="white-zone"></div>
    <div class="yellow-strip"></div>

    <div class="brand-bottom">
      <div class="brand-name"><span class="brand-mark"></span>Brightmark Electrical</div>
      <div class="brand-url">www.brightmarkelectrical.ca</div>
    </div>

    <div class="crew-photo" role="img" aria-label="Photo of four electricians in hard hats and tool belts standing together"></div>

    <footer class="footer">
      <div class="name-bar"></div>
      <div class="contact-name">DEV MARLOW</div>
      <div class="call">Call today:778-555 0142</div>
      <ul class="contact-list">
        <li><svg viewBox="0 0 20 20"><rect x="1.5" y="4" width="17" height="12" fill="none" stroke="var(--yellow)" stroke-width="1.6"/><polyline points="1.5,4 10,11 18.5,4" fill="none" stroke="var(--yellow)" stroke-width="1.6"/></svg>info@Brightmarkelectrical.ca</li>
        <li><svg viewBox="0 0 20 20"><circle cx="10" cy="10" r="8" fill="none" stroke="var(--yellow)" stroke-width="1.5"/><ellipse cx="10" cy="10" rx="3.5" ry="8" fill="none" stroke="var(--yellow)" stroke-width="1.3"/><line x1="2" y1="10" x2="18" y2="10" stroke="var(--yellow)" stroke-width="1.3"/></svg>www.Brightmarkelectrical.ca</li>
      </ul>
    </footer>
  </main>
</body>
</html>
```